Redesign the ClinWatch Website

We need a total redesign of our website, clinwatch.org. The new site should be very clean, with a flat ui, modern design. We are looking to somewhat maintain our theme colors of purple and yellow.

We require the following major changes for our site:
1. Improve searchability (add search bar)
2. Improve section layout
3. Greater emphasis on social media plug-ins
4. Redesigned font theme
5. An attractive banner that can be updated with project news
6. Website usage statistics
7. Improved usability that encourages visitors to the site to explore the various resources
and use the site’s features

Creative ideas are encouraged, with special attention given to those who create a theme for the site that is current and consistent with other top-line sites.

Specifications: The site must use only html and css (i.e. no Java), and must be easy to update frequently by staffpeople at ClinWatch.

All of the content should be taken from the website, http://clinwatch.org. However, I am attaching an updated sitemap that the designer should use. Once the winning design is chosen, I will send the site files (html, css, images, etc) so that you can populate the website with actual content.

A new logo will be provided to the designer as well.

Target Market(s)

Doctors, medical students, concerned consumers

Coding

Coded - Design and coding required

Number of Pages Required

5+ page

Font styles to use
Serif
Sans Serif

Colors
6b449b
fff3d1
fee18a
876aae
b7a5cd
fdf9cf

Requirements
Must have
• 1. Improve searchability (add search bar)
• 2. Improve section layout
• 3. Greater emphasis on social media plug-ins
• 4. Redesigned font theme
• 5. An attractive banner that can be updated with project news
• 6. Website usage statistics
• 7. Improved usability that encourages visitors to the site to explore the various resources and use the site’s features
Nice to have
• Original graphics

```html
<!DOCTYPE html>
<html lang="en">
<head>
<meta charset="utf-8">
<title>ClinWatch</title>
<link href="https://fonts.googleapis.com/css2?family=Open+Sans:wght@400;600;700&display=swap" rel="stylesheet">
<style>
:root{
  --purple-deep:#3d0f7a;
  --purple:#4b2a85;
  --purple-mid:#6b449b;
  --yellow:#fee18a;
  --yellow-soft:#fde9a6;
  --cream:#f3f0e2;
  --text:#333;
  --muted:#8a8a8a;
  --light:#a8a8a8;
  --footer:#f2f2f2;
  --bottom:#1c1c1c;
  --line:#d8d8d8;
}
*{box-sizing:border-box;margin:0;padding:0}
html,body{width:870px;height:1200px;overflow:hidden;background:#fff}
body{font-family:"Open Sans",sans-serif;color:var(--text);position:relative}
a{color:inherit;text-decoration:none}
.abs{position:absolute}

/* header */
.site-header{position:absolute;left:0;top:0;width:870px;height:62px;background:linear-gradient(#3f0c83,#5a1e9a)}
.brand{position:absolute;left:72px;top:14px;height:35px;display:flex;align-items:center;gap:6px;font-weight:700;font-size:16px;color:var(--yellow)}
.brand-dot{width:12px;height:12px;border-radius:50%;background:var(--yellow)}
.main-nav{position:absolute;top:25px;left:0;font-size:9px;font-weight:600;color:#e7dcf5;text-transform:uppercase}
.main-nav a{position:absolute;white-space:nowrap}
.main-nav a.active{color:var(--yellow)}
.search{position:absolute;left:702px;top:19px;width:96px;height:24px;border:1px solid #9b7ccc;font-size:8px;color:#b7a5cd;padding:6px 9px}
.search svg{position:absolute;right:7px;top:7px}

/* hero */
.hero{position:absolute;left:0;top:62px;width:870px;height:342px;background:linear-gradient(180deg,#b97a3e 0%,#a8682f 45%,#3f5fb4 62%,#2f55ad 100%)}
.hero-arrow{position:absolute;top:159px;width:19px;height:24px;background:rgba(0,0,0,.35);display:flex;align-items:center;justify-content:center}

/* welcome */
.welcome-title{position:absolute;top:439px;width:870px;text-align:center;font-size:18.5px;font-weight:700;color:var(--purple)}
.welcome-text{position:absolute;left:145px;top:468px;width:580px;text-align:center;font-size:9.6px;line-height:16px;color:var(--muted)}
.btn{position:absolute;top:527px;width:84px;height:29px;background:var(--yellow-soft);border-radius:2px;font-size:10px;font-weight:600;color:#4d3a1a;display:flex;align-items:center;justify-content:center}

/* news */
.news{position:absolute;left:71px;top:587px;width:727px;height:131px;background:var(--cream)}
.news-photo{position:absolute;left:6px;top:6px;width:168px;height:119px;background:linear-gradient(135deg,#2a3a5a,#b44a30 45%,#3a6cc0)}
.news-title{position:absolute;left:191px;top:18px;font-size:11.2px;color:var(--purple)}
.news-date{position:absolute;left:192px;top:38px;font-size:8px;color:#777}
.news-text{position:absolute;left:192px;top:55px;width:520px;font-size:7.6px;line-height:13.6px;color:var(--muted)}
.slide-arrow{position:absolute;top:641px}

/* columns */
.section-title{position:absolute;top:742px;font-size:15px;font-weight:700;color:var(--purple)}
.events{position:absolute;left:72px;top:772px;width:175px;height:182px;border:1px solid #ccc;border-top:3px solid var(--purple)}
.event{position:relative;height:89px;border-bottom:1px solid #ccc}
.event:last-child{border-bottom:0}
.event-date{position:absolute;left:11px;top:11px;width:30px;text-align:center;font-weight:700;line-height:1}
.event-date .m{font-size:8px;display:block}
.event-date .d{font-size:14px;display:block}
.event-sep{position:absolute;left:42px;top:10px;height:70px;border-left:1px solid #ddd}
.event-title{position:absolute;left:57px;top:10px;width:110px;font-size:9px;line-height:14px;color:#222}
.event-text{position:absolute;left:57px;top:43px;width:110px;font-size:7.6px;line-height:12px;color:var(--light)}
.project-rule{position:absolute;left:271px;top:772px;width:527px;height:2px;background:var(--purple)}
.project-photo{position:absolute;left:271px;top:780px;width:141px;height:174px;background:linear-gradient(135deg,#dfe2e8,#b7bfd2 50%,#e8e6ee)}
.project-title{position:absolute;left:424px;top:788px;font-size:9.3px;color:#222}
.project-text{position:absolute;left:425px;top:807px;width:370px;font-size:7.6px;line-height:13.6px;color:var(--muted)}
.project-text p+p{margin-top:6px}
.more{position:absolute;left:426px;top:935px;width:35px;height:19px;background:#e6e6e6;font-size:8px;color:#444;display:flex;align-items:center;justify-content:center}

/* footer */
.footer{position:absolute;left:0;top:988px;width:870px;height:146px;background:var(--footer)}
.f-head{position:absolute;top:23px;font-size:9.6px;color:#444}
.f-head.big{font-size:12.5px;top:20px}
.f-list{position:absolute;top:45px;list-style:none;font-size:7.4px;color:#888;line-height:16.2px}
.f-list li::before{content:"• ";color:#aaa}
.f-divider{position:absolute;top:22px;height:98px;border-left:1px solid #d6d6d6}
.tweet{position:absolute;left:88px;top:45px;width:130px;font-size:7.8px;line-height:12.4px;color:#888}
.tweet a{color:#3a73c9;text-decoration:underline}
.tweet .when{font-size:7px;color:#999}
.email{position:absolute;left:684px;top:43px;width:114px;height:19px;border:1px solid #ddd;background:#fff;font-size:7px;color:#777;padding:4px 8px}
.email span{position:absolute;right:0;top:0;width:26px;height:17px;background:#ddd;display:flex;align-items:center;justify-content:center}
.social{position:absolute;top:104px;width:13px;height:13px;border-radius:2px}

/* bottom */
.bottom{position:absolute;left:0;top:1134px;width:870px;height:66px;background:var(--bottom)}
.copyright{position:absolute;left:73px;top:30px;font-size:7.6px;color:#aaa}
.round{position:absolute;top:23px;width:20px;height:20px;border:1.5px solid #eee;border-radius:50%;display:flex;align-items:center;justify-content:center}
</style>
</head>
<body>

<header class="site-header">
  <div class="brand"><span class="brand-dot"></span>ClinWatch</div>
  <nav class="main-nav">
    <a class="active" style="left:262px">Home</a>
    <a style="left:316px">About us</a>
    <a style="left:386px">Events</a>
    <a style="left:445px">Resources</a>
    <a style="left:521px">Connect with us</a>
    <a style="left:628px">Contact us</a>
  </nav>
  <div class="search">Search
    <svg width="9" height="9" viewBox="0 0 10 10"><circle cx="4" cy="4" r="3" fill="none" stroke="#b7a5cd" stroke-width="1.3"/><line x1="6.3" y1="6.3" x2="9" y2="9" stroke="#b7a5cd" stroke-width="1.3"/></svg>
  </div>
</header>

<section class="hero" role="img" aria-label="Panel of four speakers seated at a blue-draped conference table with microphones">
  <span class="hero-arrow" style="left:0"><svg width="8" height="12"><polyline points="7,1 1,6 7,11" fill="none" stroke="#fff" stroke-width="1.2"/></svg></span>
  <span class="hero-arrow" style="right:0"><svg width="8" height="12"><polyline points="1,1 7,6 1,11" fill="none" stroke="#fff" stroke-width="1.2"/></svg></span>
</section>

<h1 class="welcome-title">WELCOME TO CLINWATCH</h1>
<p class="welcome-text">ClinWatch is a Halden University Medical Center project that advances evidence-based prescribing and educates healthcare professionals about pharmaceutical marketing practices. ClinWatch promotes evidence-based medicine by providing slideshows, videos, events, and links to pharma-free CME courses.</p>
<a class="btn" style="left:346px">Learn more</a>
<a class="btn" style="left:439px">Make a gift</a>

<svg class="slide-arrow" style="left:49px" width="12" height="22"><polyline points="10,1 2,11 10,21" fill="none" stroke="#bbb" stroke-width="1.5"/></svg>
<article class="news">
  <div class="news-photo" role="img" aria-label="Protester in a red hat and blue cape at a public demonstration"></div>
  <h2 class="news-title">Phasellus lorem risus, volutpat at sollicitudin</h2>
  <div class="news-date">Apr 3, 2015</div>
  <p class="news-text">Aenean aliquet risus metus, vitae tristique enim finibus eu. Sed iaculis nisl est, vitae sagittis risus fermentum sed. Donec lobortis, dui sed eleifend pellentesque, erat dui tincidunt urna, eu eleifend ante felis quis enim. Nam et turpis non turpis cursus rhoncus a et urna. Nunc tristique nec tortor vitae imperdiet. Sed elementum odio nunc, gravida mattis lorem interdum tempor. Etiam consequat lacus a felis viverra, eget rhoncus massa ullamcorper. Sed quis tincidunt neque.</p>
</article>
<svg class="slide-arrow" style="left:809px" width="12" height="22"><polyline points="2,1 10,11 2,21" fill="none" stroke="#bbb" stroke-width="1.5"/></svg>

<h2 class="section-title" style="left:72px">Upcoming Events</h2>
<div class="events">
  <div class="event">
    <div class="event-date"><span class="m">APR</span><span class="d">30</span></div>
    <span class="event-sep"></span>
    <div class="event-title">Phasellus blandit quam a ipsum gravida dapibus.</div>
    <div class="event-text">Suspendisse elit ligula, iacu-lis dignissim justo eu, vestib-ulum venenatis elit.</div>
  </div>
  <div class="event">
    <div class="event-date"><span class="m">APR</span><span class="d">30</span></div>
    <span class="event-sep"></span>
    <div class="event-title">Phasellus blandit quam a ipsum gravida dapibus.</div>
    <div class="event-text">Suspendisse elit ligula, iacu-lis dignissim justo eu, vestib-ulum venenatis elit.</div>
  </div>
</div>

<h2 class="section-title" style="left:271px">Project Details</h2>
<div class="project-rule"></div>
<div class="project-photo" role="img" aria-label="Scattered promotional pens and notepads on a table"></div>
<h3 class="project-title">Duis mattis libero augue, tempus lobortis nibh egestas sed</h3>
<div class="project-text">
  <p>Aenean aliquet risus metus, vitae tristique enim finibus eu. Sed iaculis nisl est, vitae sagittis risus fermentum sed. Donec lobortis, dui sed eleifend pellentesque, erat dui tincidunt urna, eu eleifend ante felis quis enim. Nam et turpis non turpis cursus rhoncus a et urna. Nunc tristique nec tortor vitae imperdiet. Sed elementum odio nunc, gravida mattis lorem interdum tempor.</p>
  <p>Etiam consequat lacus a felis viverra, eget rhoncus massa ullamcorper. Sed quis tincidunt neque. Pellentesque scelerisque auctor erat, at faucibus enim sollicitudin condimentum. Suspendisse eu enim ut lectus cursus commodo aliquet porta eros. Aenean tortor metus, venenatis eu luctus et, aliquet at tortor. Morbi at lectus est. Donec eu erat id purus lobortis lobortis.</p>
</div>
<a class="more">More</a>

<footer class="footer">
  <div class="f-head" style="left:73px">Latest Tweet`s</div>
  <svg class="abs" style="left:74px;top:48px" width="9" height="8" viewBox="0 0 9 8"><path d="M1 6 L8 1 L7 7 Z" fill="#aaa"/></svg>
  <p class="tweet">Praesent convallis placerat lorem, quis tincidunt lorem feugiat ut. Morbi ac <a>purus consectetur purus blandit vehicula non</a> a dolor. Mauris quis lacus ut purus<br><span class="when">Apr 30, 2015</span></p>
  <span class="f-divider" style="left:239px"></span>

  <div class="f-head" style="left:273px">Links</div>
  <ul class="f-list" style="left:274px"><li>Home</li><li>About us</li><li>Events</li><li>Resources</li><li>Connect with us</li></ul>
  <ul class="f-list" style="left:367px"><li>Contact us</li><li>FAQ</li></ul>

  <div class="f-head" style="left:459px">Other Links</div>
  <ul class="f-list" style="left:460px"><li>Terms of Uss</li><li>Privacy Policy</li><li>Help</li><li>Sitemap</li></ul>
  <div class="f-head" style="left:565px">Other Links</div>
  <ul class="f-list" style="left:566px"><li>Terms of Uss</li><li>Privacy Policy</li><li>Help</li><li>Sitemap</li></ul>
  <span class="f-divider" style="left:655px"></span>

  <div class="f-head big" style="left:686px">Newsletter</div>
  <div class="email">E-mail<span><svg width="9" height="10"><polygon points="1,0 9,5 1,10" fill="#888"/></svg></span></div>
  <div class="f-head big" style="left:686px;top:81px">Follow us on</div>
  <span class="social" style="left:684px;background:#5a7fc4"></span>
  <span class="social" style="left:712px;background:#777"></span>
  <span class="social" style="left:740px;background:#777"></span>
  <svg class="abs" style="left:767px;top:106px" width="15" height="11" viewBox="0 0 15 11"><rect width="15" height="11" rx="1" fill="#777"/><polyline points="0.5,0.5 7.5,6 14.5,0.5" fill="none" stroke="#f2f2f2" stroke-width="1.2"/></svg>
</footer>

<div class="bottom">
  <p class="copyright">Copyright &copy; 2015 &nbsp;ClinWatch. All Rights Reserved.</p>
  <span class="round" style="left:753px"><svg width="10" height="8" viewBox="0 0 10 8"><rect width="10" height="8" rx="1" fill="#fff"/><polyline points="0.5,0.5 5,4.5 9.5,0.5" fill="none" stroke="#1c1c1c"/></svg></span>
  <span class="round" style="left:778px"><svg width="8" height="10" viewBox="0 0 8 10"><polyline points="1,4 4,1 7,4" fill="none" stroke="#fff" stroke-width="1.3"/><line x1="4" y1="1" x2="4" y2="10" stroke="#fff" stroke-width="1.3"/></svg></span>
</div>

</body>
</html>
```